Roadside building business signage for a holistic health clinic.

Replace signs as shown in the attached file. They are perforated stickers that go on the windows as shown. Looking for something that has our logo and says the name of the practice with logo (Fernbrook Health & Wellness) also boldly says Acupuncture, IV Vitamins, and Holistic Health.
Possibly our phone number as well 538-207-6145

Please don't use pink except the logo. Earthy, organic tone colors appreciated.

Need of eye catching window signage of a holistic clinic on a brick building. Pink, purple, sage green, white color. Logo is pink on a white background. Please don't overload with too much pink. Words to include are "Fernbrook Health and Wellness(name of business)", "Direct Primary Care", " Medical acupuncture", "IV Vitamin Therapy", "fernbrookwholecare-example.com","538-207-6145".

Target Market(s)

People will see in their cars passing by the building. Busy roadside so need to be visible while passing in fast speed.

Industry/Entity Type

Health & Wellness

Font styles to use
Sans Serif

Colors

Designer to choose colors to be used in the design.

Requirements
Must have
• On sign must have words Holistic Medicine, Medical Acupuncture, Direct Primary Care and IV vitamins.
Nice to have
• Simple, minimalistic, artistic yet has clear message. White, Black, Violet, Pink (logo), Dark green, Sage green.
Should not have
• Bold colors (red, yellow, blue), same tone colors. Blue waves on the current signage (uploaded file) must go.

```html
<!DOCTYPE html>
<html lang="en">
<head>
<meta charset="utf-8">
<title>Fernbrook Health &amp; Wellness – Window Signage</title>
<link rel="stylesheet" href="https://fonts.googleapis.com/css2?family=Josefin+Sans:wght@400;600&family=Montserrat:ital,wght@0,500;0,600;1,700;1,800&display=swap">
<style>
:root{
  --bg:#000;
  --paper:#fff;
  --sage:#5e8a6e;
  --forest:#0f4a3a;
  --mauve:#8c5a70;
  --mauve-soft:#e6d8de;
  --pink:#e0559a;
  --ink:#1d1d1d;
}
*{margin:0;padding:0;box-sizing:border-box}
html,body{width:1200px;height:2162px;overflow:hidden;background:var(--bg)}
.signage{position:absolute;left:20px;top:650px;width:1250px;height:930px;transform:scale(.928);transform-origin:0 0;font-family:"Josefin Sans",sans-serif}
.pane{position:absolute;background:var(--paper);overflow:hidden}

/* arch */
.arch{position:absolute;left:315px;top:0;width:620px;height:300px}
.arch svg{position:absolute;inset:0}
.arch-text{position:absolute;top:78px;font-family:"Josefin Sans",sans-serif;font-size:40px;line-height:52px;color:var(--sage);letter-spacing:.5px;font-weight:400}
.arch-text.left{right:335px;text-align:right}
.arch-text.right{left:333px;text-align:left}

/* row positions */
.row1{top:310px;height:307px}
.row2{top:627px;height:303px}
.col1{left:0;width:305px}
.col2{left:315px;width:305px}
.col3{left:630px;width:305px}
.col4{left:945px;width:305px}

/* edge stripes */
.stripes-left{position:absolute;left:0;top:0;bottom:0;width:20px;
  background:linear-gradient(90deg,var(--mauve) 0 4px,transparent 4px 8px,var(--sage) 8px 11px,transparent 11px 15px,var(--sage) 15px 18px,transparent 18px)}
.stripes-right{position:absolute;right:0;top:0;bottom:0;width:20px;
  background:linear-gradient(270deg,var(--mauve) 0 4px,transparent 4px 8px,var(--sage) 8px 11px,transparent 11px 15px,var(--sage) 15px 18px,transparent 18px)}
.stripes-bottom{position:absolute;left:0;right:0;bottom:0;height:16px;
  background:linear-gradient(0deg,var(--mauve) 0 4px,transparent 4px 7px,var(--sage) 7px 10px,transparent 10px 13px,var(--sage) 13px 16px)}

/* brand panels */
.ribbon{position:absolute;left:105px;top:0;width:85px;height:80px;background:linear-gradient(180deg,#b38797,#efe3e8)}
.sprig{position:absolute;top:0;width:105px;height:70px;background:radial-gradient(ellipse at 60% 30%,#6f8f78 0,#a9bfad 55%,rgba(255,255,255,0) 75%)}
.brand-panel .sprig{right:0}
.brand-mark{position:absolute;left:0;right:0;top:100px;text-align:center}
.brand-dot{display:block;margin:0 auto 10px;width:44px;height:44px;border-radius:50%;background:var(--pink)}
.brand-name{font-family:"Josefin Sans",sans-serif;font-weight:600;font-size:26px;letter-spacing:3px;color:var(--forest);line-height:1}
.brand-sub{font-family:"Josefin Sans",sans-serif;font-weight:600;font-size:9px;letter-spacing:2px;color:var(--forest);margin-top:4px}
.service-tag{position:absolute;left:0;right:0;top:220px;text-align:center;font-family:"Montserrat",sans-serif;font-style:italic;font-weight:800;font-size:22px;line-height:28px;color:var(--mauve)}

/* photo panels */
.photo{position:absolute;inset:0;background:linear-gradient(180deg,#d8e8e6 0%,#b9d3d8 38%,#7fb0bf 58%,#e9dccd 80%,#c9a884 100%)}
.photo-mark{position:absolute;top:14px;text-align:center;width:120px}
.photo-mark .brand-dot{width:36px;height:36px;margin-bottom:8px}
.photo-mark .brand-name{font-size:20px;letter-spacing:2px}
.col2 .photo-mark{left:30px}
.col3 .photo-mark{right:30px}

/* benefits panels */
.benefits{position:absolute;left:20px;right:20px;top:44px;text-align:center;font-family:"Montserrat",sans-serif;font-style:italic;font-weight:700;font-size:12.5px;line-height:19px}
.benefits li{list-style:none}
.benefits li:nth-child(odd){color:var(--forest)}
.benefits li:nth-child(even){color:var(--mauve)}
.join{position:absolute;left:50%;top:180px;transform:translateX(-50%);background:var(--forest);color:#fff;font-family:"Montserrat",sans-serif;font-weight:600;font-size:9px;letter-spacing:.5px;padding:6px 14px;white-space:nowrap}
.contact{position:absolute;left:0;right:0;top:214px;text-align:center;font-family:"Montserrat",sans-serif;font-weight:500;color:var(--ink)}
.contact .phone{font-size:14px;letter-spacing:1.5px;line-height:18px}
.contact .address{font-size:11px;letter-spacing:1px;line-height:14px}
.contact .web{font-size:11px;letter-spacing:1px;color:var(--mauve);margin-top:12px}

/* services panels */
.services-glow{position:absolute;left:50%;top:0;transform:translateX(-50%);width:200px;height:70px;border-radius:0 0 40px 40px;background:linear-gradient(180deg,#d7c1ca,rgba(255,255,255,0))}
.services{position:absolute;left:50%;top:40px;transform:translateX(-50%);width:185px;text-align:center;font-size:17px;color:var(--ink)}
.services li{list-style:none;padding:7px 0 6px;border-bottom:1.5px dotted var(--mauve)}
.services li:last-child{border-bottom:none}
.headline-box{position:absolute;left:28px;right:28px;top:180px;border:1.5px solid var(--mauve);border-radius:6px;padding:4px 0;text-align:center;font-family:"Montserrat",sans-serif;font-style:italic;font-weight:800;font-size:14px;line-height:18px;color:var(--mauve)}
.services-contact{position:absolute;left:0;right:0;top:233px;text-align:center;font-family:"Montserrat",sans-serif;font-weight:500}
.services-contact .phone{font-size:14px;letter-spacing:1.5px;color:var(--ink)}
.services-contact .web{font-size:11px;letter-spacing:1px;color:var(--mauve);margin-top:3px}
</style>
</head>
<body>
<main class="signage">

  <section class="arch">
    <svg viewBox="0 0 620 300" width="620" height="300" aria-hidden="true">
      <path d="M0 300 V200 C0 90 140 0 310 0 C480 0 620 90 620 200 V300 Z" fill="#fff" stroke="#8c5a70" stroke-width="6"/>
      <path d="M10 300 V200 C10 96 146 10 310 10 C474 10 610 96 610 200 V300" fill="none" stroke="#5e8a6e" stroke-width="3"/>
      <path d="M18 300 V200 C18 101 151 18 310 18 C469 18 602 101 602 200 V300" fill="none" stroke="#5e8a6e" stroke-width="3"/>
      <rect x="305" y="0" width="10" height="300" fill="#000"/>
    </svg>
    <p class="arch-text left">DIRECT<br>HOLISTIC<br>PRIMARY<br>CARE</p>
    <p class="arch-text right">DIRECT<br>HOLISTIC<br>PRIMARY<br>CARE</p>
  </section>

  <!-- row one -->
  <section class="pane row1 col1 brand-panel">
    <div class="stripes-left"></div>
    <div class="ribbon"></div>
    <div class="sprig" role="img" aria-label="Eucalyptus sprig"></div>
    <div class="brand-mark">
      <span class="brand-dot"></span>
      <div class="brand-name">FERNBROOK</div>
      <div class="brand-sub">HEALTH &amp; WELLNESS</div>
    </div>
    <p class="service-tag">DIRECT<br>PRIMARY CARE</p>
  </section>

  <section class="pane row1 col2">
    <div class="photo" role="img" aria-label="Woman in white seated on a lakeside beach, meditating"></div>
    <div class="photo-mark">
      <span class="brand-dot"></span>
      <div class="brand-name">FERNBROOK</div>
    </div>
  </section>

  <section class="pane row1 col3">
    <div class="photo" role="img" aria-label="Woman in white seated on a lakeside beach, meditating"></div>
    <div class="photo-mark">
      <span class="brand-dot"></span>
      <div class="brand-name">FERNBROOK</div>
    </div>
  </section>

  <section class="pane row1 col4 brand-panel">
    <div class="stripes-right"></div>
    <div class="ribbon"></div>
    <div class="sprig" role="img" aria-label="Eucalyptus sprig" style="left:0;right:auto"></div>
    <div class="brand-mark">
      <span class="brand-dot"></span>
      <div class="brand-name">FERNBROOK</div>
      <div class="brand-sub">HEALTH &amp; WELLNESS</div>
    </div>
    <p class="service-tag">DIRECT<br>PRIMARY CARE</p>
  </section>

  <!-- row two -->
  <section class="pane row2 col1">
    <div class="stripes-left"></div>
    <ul class="benefits">
      <li>30-90 Minutes Relaxed Appointment</li>
      <li>Price Transparency no Copays</li>
      <li>Minimal Wait Times</li>
      <li>Direct communication with your Physician</li>
      <li>Easy to Book Appointment</li>
    </ul>
    <span class="join">JOIN US TODAY!</span>
    <div class="contact">
      <p class="phone">538-207-6145</p>
      <p class="address">1420 N Alder Rd., STE 2B</p>
      <p class="address">Riverton, IN 46032</p>
      <p class="web">fernbrookwholecare-example.com</p>
    </div>
  </section>

  <section class="pane row2 col2">
    <div class="services-glow"></div>
    <ul class="services">
      <li>Holistic Medicine</li>
      <li>Direct Primary Care</li>
      <li>Medical acupuncture</li>
      <li>IV Vitamin Therapy</li>
    </ul>
    <p class="headline-box">Acupuncture, IV Vitamins<br>and Holistic Health.</p>
    <div class="services-contact">
      <p class="phone">538-207-6145</p>
      <p class="web">fernbrookwholecare-example.com</p>
    </div>
    <div class="stripes-bottom"></div>
  </section>

  <section class="pane row2 col3">
    <div class="services-glow"></div>
    <ul class="services">
      <li>Holistic Medicine</li>
      <li>Direct Primary Care</li>
      <li>Medical acupuncture</li>
      <li>IV Vitamin Therapy</li>
    </ul>
    <p class="headline-box">Acupuncture, IV Vitamins<br>and Holistic Health.</p>
    <div class="services-contact">
      <p class="phone">538-207-6145</p>
      <p class="web">fernbrookwholecare-example.com</p>
    </div>
    <div class="stripes-bottom"></div>
  </section>

  <section class="pane row2 col4">
    <div class="stripes-right"></div>
    <ul class="benefits">
      <li>30-90 Minutes Relaxed Appointment</li>
      <li>Price Transparency no Copays</li>
      <li>Minimal Wait Times</li>
      <li>Direct communication with your Physician</li>
      <li>Easy to Book Appointment</li>
    </ul>
    <span class="join">JOIN US TODAY!</span>
    <div class="contact">
      <p class="phone">538-207-6145</p>
      <p class="address">1420 N Alder Rd., STE 2B</p>
      <p class="address">Riverton, IN 46032</p>
      <p class="web">fernbrookwholecare-example.com</p>
    </div>
  </section>

</main>
</body>
</html>
```